Powerpoint for consulting dentalpractices on management, improvement, and benchmarks

Fase 1: create 8-15 slides to be used for the model. The are the basic slideexamples for future presentation.
colour scheme and font types as in attachment for older powerpoint. Fonts, logo and colourscheme stay the same. Newer slidedeck contains newer ideas for new presentations. Smaller logo maybe better to be used for all slides. Normal logo for starting and end slide. Open for your inspiration and new suggestions
Fase 2 create slidemaster to enable us to create new slidedesks faster.

Target Market(s)

Dentalpractices (no dental images in powerpoint)

Industry/Entity Type

Dental practices

Font styles to use
Other font styles liked:
• Roobert for heading Normal Text Inter

Requirements
Must have
• Different slidemaster basic slides to quickly create slides with full slide pictures which still have a Molvera touch. Content slides, slides with bullets and slides to show 3 -5 subjects
Nice to have
• New styling element for recognition of brand
Should not have
• round edges, complex slide master

```html
<!DOCTYPE html>
<html lang="en">
<head>
<meta charset="utf-8">
<title>Molvera – slide template overview</title>
<link href="https://fonts.googleapis.com/css2?family=Inter:wght@300;400;500;600;700&family=Manrope:wght@500;600;700;800&display=swap" rel="stylesheet">
<style>
  :root {
    --canvas: #d3e3d3;
    --green: #77bf1a;
    --green-soft: #8cc63f;
    --green-pale: #c6e29c;
    --blue: #1b4f9c;
    --ink: #333b44;
    --grey: #e6e8e8;
    --white: #ffffff;
  }
  * { margin: 0; padding: 0; box-sizing: border-box; }
  html, body { width: 1200px; height: 600px; overflow: hidden; background: var(--canvas); }
  .deck { position: relative; width: 1200px; height: 600px; }
  .slide {
    position: absolute; width: 247px; height: 139px; background: var(--white);
    box-shadow: 0 3px 6px rgba(40, 70, 40, 0.18);
    overflow: hidden;
  }
  .slide svg { display: block; width: 100%; height: 100%; }
  .c1 { left: 82px; } .c2 { left: 348px; } .c3 { left: 613px; } .c4 { left: 878px; }
  .r1 { top: 74px; } .r2 { top: 231px; } .r3 { top: 389px; }

  .heading { font-family: "Inter", sans-serif; font-size: 13px; fill: var(--blue); font-weight: 400; }
  .display { font-family: "Manrope", sans-serif; font-weight: 700; letter-spacing: 4px; }
  .brand { font-family: "Inter", sans-serif; font-size: 50px; font-weight: 500; fill: var(--blue); letter-spacing: -1px; }
  .body { font-family: "Inter", sans-serif; font-size: 5.4px; fill: var(--ink); }
  .body-white { font-family: "Inter", sans-serif; font-size: 4.4px; fill: var(--white); }
  .sub { font-family: "Inter", sans-serif; font-size: 7px; fill: var(--ink); }
  .lead { font-family: "Inter", sans-serif; font-size: 5.4px; font-style: italic; font-weight: 600; fill: var(--blue); }
  .kicker { font-family: "Inter", sans-serif; font-size: 6px; font-weight: 700; fill: var(--green); }
  .label { font-family: "Inter", sans-serif; font-size: 6px; fill: var(--blue); }
  .tier { font-family: "Inter", sans-serif; font-size: 11px; font-weight: 300; fill: var(--white); letter-spacing: 1px; }
  .tiny-white { font-family: "Inter", sans-serif; font-size: 4.6px; fill: var(--white); }
  .photo-blue { fill: url(#gBlue); }
</style>
</head>
<body>
<svg width="0" height="0" style="position:absolute" aria-hidden="true">
  <defs>
    <linearGradient id="gLab" x1="0" y1="0" x2="1" y2="1"><stop offset="0" stop-color="#dfe9f0"/><stop offset="1" stop-color="#8aa7bd"/></linearGradient>
    <linearGradient id="gBlue" x1="0" y1="0" x2="1" y2="1"><stop offset="0" stop-color="#a8d2e8"/><stop offset="1" stop-color="#4d8fb8"/></linearGradient>
    <linearGradient id="gPills" x1="0" y1="0" x2="1" y2="1"><stop offset="0" stop-color="#d9c9d0"/><stop offset="0.5" stop-color="#e07aa8"/><stop offset="1" stop-color="#c9c3c6"/></linearGradient>
    <linearGradient id="gScan" x1="0" y1="0" x2="1" y2="1"><stop offset="0" stop-color="#c9cede"/><stop offset="0.45" stop-color="#4f5ee0"/><stop offset="1" stop-color="#2a2f8c"/></linearGradient>
    <linearGradient id="gStone" x1="0" y1="0" x2="1" y2="1"><stop offset="0" stop-color="#c9c6c1"/><stop offset="1" stop-color="#8e8a84"/></linearGradient>
    <linearGradient id="gStairs" x1="0" y1="0" x2="1" y2="1"><stop offset="0" stop-color="#8cc63f"/><stop offset="1" stop-color="#2f62a8"/></linearGradient>
  </defs>
</svg>

<main class="deck">

  <!-- Cover -->
  <section class="slide c1 r1">
    <svg viewBox="0 0 530 298">
      <g fill="none" stroke="var(--green)" stroke-width="3">
        <polygon points="43,45 63,10 103,10 123,45 103,80 63,80"/>
        <polygon points="11,48 23,27 47,27 59,48 47,69 23,69"/>
        <polygon points="-26,233 -8,202 28,202 46,233 28,264 -8,264"/>
        <polygon points="283,275 294.5,255 317.5,255 329,275 317.5,295 294.5,295"/>
        <polygon points="414,32 425,13 447,13 458,32 447,51 425,51"/>
        <polygon points="465,12 480,-14 510,-14 525,12 510,38 480,38"/>
      </g>
      <polygon points="258,0 440,0 400,80 300,80" fill="var(--green)"/>
      <polygon points="455,298 530,228 530,298" fill="var(--green)"/>
      <polygon points="472,253 481,237 499,237 508,253 499,269 481,269" fill="none" stroke="var(--white)" stroke-width="2.5"/>
      <text class="brand" x="84" y="184">Molvera</text>
      <text class="heading" x="358" y="152" style="font-size:20px">Title of the</text>
      <text class="heading" x="358" y="174" style="font-size:20px">presentation</text>
      <rect x="358" y="186" width="128" height="2.5" fill="var(--blue)"/>
    </svg>
  </section>

  <!-- Intro with diamond image -->
  <section class="slide c2 r1">
    <svg viewBox="0 0 530 298">
      <polygon points="0,0 128,0 40,92 0,55" fill="var(--green)"/>
      <polygon points="122,78 198,154 122,230 46,154" fill="url(#gLab)" role="img" aria-label="Laboratory microscope photo"/>
      <polyline points="46,170 122,246 198,170" fill="none" stroke="var(--green)" stroke-width="12"/>
      <rect x="266" y="0" width="6" height="40" fill="var(--green)"/>
      <rect x="266" y="212" width="6" height="86" fill="var(--green)"/>
      <polygon points="470,0 530,0 530,58 490,58 468,22" fill="var(--green)"/>
      <polygon points="460,48 470,30 490,30 500,48 490,66 470,66" fill="none" stroke="var(--green-pale)" stroke-width="1.5"/>
      <polygon points="432,4 440,-10 456,-10 464,4 456,18 440,18" fill="none" stroke="var(--green-pale)" stroke-width="1.5"/>
      <text class="heading" x="264" y="70">Title here</text>
      <g class="body">
        <text x="264" y="116">Lorem ipsum dolor sit amet, consectetuer adipiscing elit, sed diam nonum-</text>
        <text x="264" y="123">my nibh euismod tincidunt ut laoreet dolore magna aliquam erat volutpat.</text>
        <text x="264" y="130">Ut wisi enim ad minim veniam, quis nostrud exerci tation ullamcorper</text>
        <text x="264" y="137">suscipit lobortis nisl ut aliquip ex ea commodo consequat. Duis autem vel</text>
        <text x="264" y="144">eum iriure dolor in hendrerit in vulputate velit esse molestie consequat.</text>
        <text x="264" y="162">Lorem ipsum dolor sit amet, consectetuer adipiscing elit, sed diam nonum-</text>
        <text x="264" y="169">my nibh euismod tincidunt ut laoreet dolore magna aliquam erat volutpat.</text>
        <text x="264" y="176">Ut wisi enim ad minim veniam, quis nostrud exerci tation ullamcorper</text>
        <text x="264" y="183">suscipit lobortis nisl ut aliquip ex ea commodo consequat. Duis autem vel</text>
        <text x="264" y="190">eum iriure dolor in hendrerit in vulputate velit esse molestie consequat.</text>
      </g>
    </svg>
  </section>

  <!-- Three image column -->
  <section class="slide c3 r1">
    <svg viewBox="0 0 530 298">
      <rect x="0" y="35" width="22" height="230" fill="var(--green)"/>
      <rect x="108" y="33" width="74" height="74" class="photo-blue" role="img" aria-label="Medical supplies photo"/>
      <rect x="66" y="112" width="74" height="74" class="photo-blue" role="img" aria-label="Glucose meter photo"/>
      <rect x="108" y="190" width="74" height="74" class="photo-blue" role="img" aria-label="Pills and syringe photo"/>
      <text class="heading" x="226" y="56">Title here</text>
      <g class="sub">
        <text x="226" y="100">Dolor Sit Amet</text><text x="226" y="109">(consectetuer adipiscing)</text>
        <text x="226" y="155">Dolor Sit Amet</text><text x="226" y="164">(consectetuer adipiscing)</text>
        <text x="226" y="211">Dolor Sit Amet</text><text x="226" y="220">(consectetuer adipiscing)</text>
      </g>
      <g class="body">
        <text x="226" y="123">Lorem ipsum dolor sit amet, consectetuer adipiscing elit, sed diam nonummy</text>
        <text x="226" y="130">nibh euismod tincidunt ut laoreet dolore magna aliquam erat volutpat. Ut wisi</text>
        <text x="226" y="137">enim ad minim veniam, quis nostrud exerci tation ullamcorper.</text>
        <text x="226" y="178">Lorem ipsum dolor sit amet, consectetuer adipiscing elit, sed diam nonummy</text>
        <text x="226" y="185">nibh euismod tincidunt ut laoreet dolore magna aliquam erat volutpat. Ut wisi</text>
        <text x="226" y="192">enim ad minim veniam, quis nostrud exerci tation ullamcorper.</text>
        <text x="226" y="234">Lorem ipsum dolor sit amet, consectetuer adipiscing elit, sed diam nonum-</text>
        <text x="226" y="241">my nibh euismod tincidunt ut laoreet dolore magna aliquam erat volutpat.</text>
        <text x="226" y="248">Ut wisi enim ad minim veniam, quis nostrud exerci tation ullamcorper.</text>
      </g>
    </svg>
  </section>

  <!-- Four points with image -->
  <section class="slide c4 r1">
    <svg viewBox="0 0 530 298">
      <polygon points="0,0 150,0 225,85 125,298 0,298" fill="url(#gPills)" role="img" aria-label="Pink tablets in blister packs photo"/>
      <polygon points="25,298 190,175 240,298" fill="var(--green)"/>
      <polygon points="430,0 530,0 510,62" fill="var(--green)"/>
      <text class="heading" x="258" y="66">Title here</text>
      <rect x="198" y="86" width="60" height="1.2" fill="var(--blue)"/>
      <g class="label">
        <text x="258" y="138">01</text><text x="276" y="136">Dolor Sit Amet</text>
        <text x="258" y="196">02</text><text x="276" y="194">Dolor Sit Amet</text>
        <text x="386" y="138">03</text><text x="404" y="136">Dolor Sit Amet</text>
        <text x="386" y="196">04</text><text x="404" y="194">Dolor Sit Amet</text>
      </g>
      <g class="body">
        <text x="276" y="150">Lorem ipsum dolor sit amet,</text><text x="276" y="156">consectetuer adipiscing elit,</text><text x="276" y="162">sed diam nonummy nibh</text><text x="276" y="168">euismod tincidunt ut laoreet</text><text x="276" y="174">dolore magna aliquam erat.</text>
        <text x="276" y="208">Lorem ipsum dolor sit amet,</text><text x="276" y="214">consectetuer adipiscing elit,</text><text x="276" y="220">sed diam nonummy nibh</text><text x="276" y="226">euismod tincidunt ut laoreet</text><text x="276" y="232">dolore magna aliquam erat.</text>
        <text x="404" y="150">Lorem ipsum dolor sit amet,</text><text x="404" y="156">consectetuer adipiscing elit,</text><text x="404" y="162">sed diam nonummy nibh</text><text x="404" y="168">euismod tincidunt ut laoreet</text><text x="404" y="174">dolore magna aliquam erat.</text>
        <text x="404" y="208">Lorem ipsum dolor sit amet,</text><text x="404" y="214">consectetuer adipiscing elit,</text><text x="404" y="220">sed diam nonummy nibh</text><text x="404" y="226">euismod tincidunt ut laoreet</text><text x="404" y="232">dolore magna aliquam erat.</text>
      </g>
    </svg>
  </section>

  <!-- Numbered bullets -->
  <section class="slide c1 r2">
    <svg viewBox="0 0 530 298">
      <rect x="18" y="0" width="116" height="298" fill="var(--green)"/>
      <rect x="350" y="286" width="155" height="12" fill="var(--green)"/>
      <text class="heading" x="151" y="47">Title here</text>
      <rect x="116" y="62" width="74" height="1.2" fill="var(--blue)"/>
      <g>
        <circle cx="208" cy="104" r="7" fill="var(--green)"/><text x="208" y="106" class="tiny-white" text-anchor="middle">1</text>
        <circle cx="208" cy="164" r="7" fill="var(--green)"/><text x="208" y="166" class="tiny-white" text-anchor="middle">2</text>
        <circle cx="208" cy="224" r="7" fill="var(--green)"/><text x="208" y="226" class="tiny-white" text-anchor="middle">3</text>
      </g>
      <g class="lead">
        <text x="225" y="103">Lorem ipsum dolor sit amet, consectetuer adipiscing elit</text>
        <text x="225" y="163">Lorem ipsum dolor sit amet, consectetuer adipiscing elit</text>
        <text x="225" y="223">Lorem ipsum dolor sit amet, consectetuer adipiscing elit</text>
      </g>
      <g class="body">
        <text x="225" y="122">Lorem ipsum dolor sit amet, consectetuer adipiscing elit, sed diam nonummy nibh euismod</text>
        <text x="225" y="128">tincidunt ut laoreet dolore magna aliquam erat volutpat. Ut wisi enim ad minim veniam,</text>
        <text x="225" y="134">quis nostrud exerci tation ullamcorper suscipit lobortis nisl.</text>
        <text x="225" y="182">Lorem ipsum dolor sit amet, consectetuer adipiscing elit, sed diam nonummy nibh</text>
        <text x="225" y="188">euismod tincidunt ut laoreet dolore magna aliquam erat volutpat. Ut wisi enim ad</text>
        <text x="225" y="194">minim veniam, quis nostrud exerci tation ullamcorper suscipit lobortis nisl.</text>
        <text x="225" y="242">Lorem ipsum dolor sit amet, consectetuer adipiscing elit, sed diam nonummy nibh</text>
        <text x="225" y="248">euismod tincidunt ut laoreet dolore magna aliquam erat volutpat. Ut wisi enim ad</text>
        <text x="225" y="254">minim veniam, quis nostrud exerci tation ullamcorper suscipit lobortis nisl.</text>
      </g>
    </svg>
  </section>

  <!-- Pricing tiers -->
  <section class="slide c2 r2">
    <svg viewBox="0 0 530 298">
      <rect x="0" y="162" width="530" height="118" fill="var(--grey)"/>
      <rect x="0" y="50" width="212" height="5" fill="var(--green)"/>
      <rect x="323" y="268" width="207" height="4" fill="var(--green)"/>
      <text class="heading" x="248" y="56">Title here</text>
      <rect x="248" y="67" width="40" height="1.2" fill="var(--blue)"/>
      <rect x="100" y="102" width="336" height="156" fill="var(--green-soft)"/>
      <rect x="211" y="102" width="1" height="156" fill="#a7d46a"/>
      <rect x="323" y="102" width="1" height="156" fill="#a7d46a"/>
      <text class="tier" x="155" y="128" text-anchor="middle">BASIC</text>
      <text class="tier" x="267" y="128" text-anchor="middle">STANDARD</text>
      <text class="tier" x="379" y="128" text-anchor="middle">PREMIUM</text>
      <g class="tiny-white" text-anchor="middle">
        <text x="155" y="167">Lorem ipsum dolor sit amet,</text><text x="155" y="173">consectetuer adipiscing elit,</text><text x="155" y="179">sed diam nonummy nibh</text><text x="155" y="185">euismod tincidunt ut.</text>
        <text x="155" y="219">Lorem ipsum dolor sit amet,</text><text x="155" y="225">consectetuer adipiscing elit,</text><text x="155" y="231">sed diam nonummy nibh</text><text x="155" y="237">euismod tincidunt ut.</text>
        <text x="267" y="167">Lorem ipsum dolor sit amet,</text><text x="267" y="173">consectetuer adipiscing elit,</text><text x="267" y="179">sed diam nonummy nibh</text><text x="267" y="185">euismod tincidunt ut.</text>
        <text x="267" y="219">Lorem ipsum dolor sit amet,</text><text x="267" y="225">consectetuer adipiscing elit,</text><text x="267" y="231">sed diam nonummy nibh</text><text x="267" y="237">euismod tincidunt ut.</text>
        <text x="379" y="167">Lorem ipsum dolor sit amet,</text><text x="379" y="173">consectetuer adipiscing elit,</text><text x="379" y="179">sed diam nonummy nibh</text><text x="379" y="185">euismod tincidunt ut.</text>
        <text x="379" y="219">Lorem ipsum dolor sit amet,</text><text x="379" y="225">consectetuer adipiscing elit,</text><text x="379" y="231">sed diam nonummy nibh</text><text x="379" y="237">euismod tincidunt ut.</text>
      </g>
    </svg>
  </section>

  <!-- Green panel with three steps -->
  <section class="slide c3 r2">
    <svg viewBox="0 0 530 298">
      <rect x="0" y="0" width="218" height="298" fill="var(--green-soft)"/>
      <text class="display" x="46" y="80" fill="var(--white)" style="font-size:12px;font-weight:500">Title Here</text>
      <rect x="46" y="98" width="40" height="1.2" fill="var(--white)"/>
      <g class="body-white">
        <text x="46" y="143">Lorem ipsum dolor sit amet, consectetuer adipiscing elit, sed</text>
        <text x="46" y="149">diam nonummy nibh euismod tincidunt ut laoreet dolore</text>
        <text x="46" y="155">magna aliquam erat volutpat. Ut wisi enim ad minim veniam,</text>
        <text x="46" y="161">quis nostrud exerci tation ullamcorper suscipit lobortis nisl.</text>
        <text x="46" y="190">Lorem ipsum dolor sit amet, consectetuer adipiscing elit, sed</text>
        <text x="46" y="196">diam nonummy nibh euismod tincidunt ut laoreet dolore</text>
        <text x="46" y="202">magna aliquam erat volutpat. Ut wisi enim ad minim veniam,</text>
        <text x="46" y="208">quis nostrud exerci tation ullamcorper suscipit lobortis nisl.</text>
        <text x="46" y="214">Duis autem vel eum iriure in hendrerit in vulputate velit.</text>
      </g>
      <g fill="var(--blue)">
        <rect x="252" y="18" width="14" height="14"/><rect x="250" y="36" width="40" height="2"/>
        <rect x="460" y="112" width="14" height="14"/><rect x="456" y="130" width="40" height="2"/>
        <rect x="252" y="198" width="14" height="14"/><rect x="250" y="216" width="40" height="2"/>
      </g>
      <g class="lead" style="font-size:4.4px">
        <text x="236" y="58">Lorem ipsum dolor sit amet, consectetuer</text><text x="236" y="63">adipiscing elit</text>
        <text x="500" y="153" text-anchor="end">Lorem ipsum dolor sit amet, consectetuer</text><text x="500" y="158" text-anchor="end">adipiscing elit</text>
        <text x="236" y="238">Lorem ipsum dolor sit amet, consectetuer</text><text x="236" y="243">adipiscing elit</text>
      </g>
      <g class="body" style="font-size:4.4px">
        <text x="236" y="72">Lorem ipsum dolor sit amet, consectetuer adipiscing elit, sed</text>
        <text x="236" y="78">diam nonummy nibh euismod tincidunt ut laoreet dolore magna</text>
        <text x="236" y="84">aliquam erat volutpat. Ut wisi enim ad minim veniam, quis</text>
        <text x="236" y="90">nostrud exerci tation ullamcorper suscipit lobortis nisl.</text>
        <text x="500" y="170" text-anchor="end">Lorem ipsum dolor sit amet, consectetuer adipiscing elit, sed</text>
        <text x="500" y="176" text-anchor="end">diam nonummy nibh euismod tincidunt ut laoreet dolore magna</text>
        <text x="500" y="182" text-anchor="end">aliquam erat volutpat. Ut wisi enim ad minim veniam, quis</text>
        <text x="500" y="188" text-anchor="end">nostrud exerci tation ullamcorper suscipit lobortis nisl.</text>
        <text x="236" y="254">Lorem ipsum dolor sit amet, consectetuer adipiscing elit, sed</text>
        <text x="236" y="260">diam nonummy nibh euismod tincidunt ut laoreet dolore magna</text>
        <text x="236" y="266">aliquam erat volutpat. Ut wisi enim ad minim veniam, quis</text>
        <text x="236" y="272">nostrud exerci tation ullamcorper suscipit lobortis nisl.</text>
      </g>
    </svg>
  </section>

  <!-- Table -->
  <section class="slide c4 r2">
    <svg viewBox="0 0 530 298">
      <rect x="0" y="15" width="89" height="183" fill="var(--green-soft)"/>
      <text class="heading" x="115" y="46">Title here</text>
      <rect x="80" y="58" width="82" height="1.2" fill="var(--blue)"/>
      <g class="body" style="font-size:4.6px">
        <text x="110" y="86">Lorem ipsum dolor sit amet, consectetuer adipiscing elit, sed diam nonummy nibh euismod tincidunt ut laoreet dolore magna aliquam erat</text>
        <text x="110" y="92">volutpat. Ut wisi enim ad minim veniam, quis nostrud exerci tation ullamcorper suscipit lobortis nisl ut aliquip ex ea commodo consequat. Duis</text>
        <text x="110" y="98">autem vel eum iriure dolor in hendrerit in vulputate velit esse molestie consequat.</text>
      </g>
      <rect x="110" y="132" width="362" height="10" fill="var(--blue)"/>
      <g fill="var(--white)"><rect x="183" y="132" width="1" height="10"/><rect x="402" y="132" width="1" height="10"/><rect x="436" y="132" width="1" height="10"/></g>
      <g class="tiny-white" style="font-size:4.2px">
        <text x="113" y="139">Current liabilities</text><text x="419" y="139" text-anchor="middle">2017</text><text x="454" y="139" text-anchor="middle">2018</text>
      </g>
      <g fill="#f1f2f2">
        <rect x="110" y="143" width="362" height="10"/><rect x="110" y="167" width="362" height="10"/><rect x="110" y="191" width="362" height="10"/><rect x="110" y="215" width="362" height="10"/><rect x="110" y="239" width="362" height="10"/><rect x="110" y="263" width="362" height="10"/>
      </g>
      <g fill="#e2e4e4">
        <rect x="110" y="154" width="362" height="0.6"/><rect x="110" y="178" width="362" height="0.6"/><rect x="110" y="202" width="362" height="0.6"/><rect x="110" y="226" width="362" height="0.6"/><rect x="110" y="250" width="362" height="0.6"/><rect x="110" y="274" width="362" height="0.6"/>
        <rect x="183" y="143" width="0.6" height="138"/><rect x="402" y="143" width="0.6" height="138"/><rect x="436" y="143" width="0.6" height="138"/>
      </g>
    </svg>
  </section>

  <!-- Full image section divider -->
  <section class="slide c1 r3">
    <svg viewBox="0 0 530 298">
      <rect x="0" y="0" width="530" height="298" fill="url(#gScan)" role="img" aria-label="Patient in radiotherapy scanner photo"/>
      <rect x="388" y="0" width="7" height="60" fill="var(--white)"/>
      <rect x="388" y="198" width="7" height="100" fill="var(--white)"/>
      <text class="display" x="385" y="144" fill="var(--white)" style="font-size:14px">Chemo of</text>
      <text class="display" x="385" y="158" fill="var(--white)" style="font-size:14px">bestraling</text>
      <rect x="350" y="170" width="75" height="1.5" fill="var(--white)"/>
    </svg>
  </section>

  <!-- Bar chart -->
  <section class="slide c2 r3">
    <svg viewBox="0 0 530 298">
      <rect x="32" y="57" width="188" height="193" fill="var(--grey)"/>
      <rect x="55" y="0" width="48" height="188" fill="var(--green-soft)"/>
      <rect x="228" y="57" width="260" height="193" fill="var(--green-soft)"/>
      <rect x="483" y="57" width="47" height="241" fill="var(--green-soft)"/>
      <text class="display" x="122" y="97" fill="var(--blue)" style="font-size:11px;letter-spacing:2.5px">Dolor</text>
      <text class="display" x="122" y="110" fill="var(--blue)" style="font-size:11px;letter-spacing:2.5px">Sit Amet</text>
      <rect x="88" y="120" width="70" height="1.2" fill="var(--blue)"/>
      <g class="body" style="font-size:3.8px">
        <text x="122" y="143">Lorem ipsum dolor sit amet, consectetuer</text><text x="122" y="148">adipiscing elit, sed diam nonummy nibh</text><text x="122" y="153">euismod tincidunt ut laoreet dolore magna</text><text x="122" y="158">aliquam erat volutpat. Ut wisi enim ad</text><text x="122" y="163">minim veniam, quis nostrud exerci tation</text><text x="122" y="168">ullamcorper suscipit lobortis nisl ut aliquip</text><text x="122" y="173">ex ea commodo consequat.</text>
        <text x="122" y="186">Duis autem vel eum iriure dolor in</text><text x="122" y="191">hendrerit in vulputate velit esse molestie</text><text x="122" y="196">consequat, vel illum dolore eu feugiat nulla</text><text x="122" y="201">facilisis at vero eros et accumsan et iusto</text><text x="122" y="206">odio dignissim qui.</text>
      </g>
      <g fill="var(--green-pale)">
        <rect x="253" y="204" width="30" height="32"/>
        <rect x="295" y="174" width="30" height="62"/>
        <rect x="337" y="116" width="30" height="120"/>
        <rect x="379" y="132" width="30" height="104"/>
        <rect x="421" y="78" width="30" height="158"/>
      </g>
      <g class="tiny-white" text-anchor="middle">
        <text x="268" y="213">15%</text><text x="310" y="183">27%</text><text x="352" y="125">58%</text><text x="394" y="141">47%</text><text x="436" y="87">82%</text>
      </g>
      <g class="tiny-white" text-anchor="middle" style="font-size:3.6px;font-weight:700">
        <text x="268" y="245">Dolor Sit</text><text x="310" y="245">Sit Amet</text><text x="352" y="245">Dolor Sit</text><text x="394" y="245">Sit Amet</text><text x="436" y="245">Dolor Sit</text>
      </g>
    </svg>
  </section>

  <!-- Five takeaways -->
  <section class="slide c3 r3">
    <svg viewBox="0 0 530 298">
      <rect x="0" y="22" width="188" height="48" fill="var(--green-soft)"/>
      <text class="heading" x="212" y="49">5 takeaways</text>
      <rect x="212" y="60" width="40" height="1.2" fill="var(--blue)"/>
      <g fill="none" stroke="var(--green-soft)" stroke-width="2.5">
        <polygon points="404,37 424,2 464,2 484,37 464,72 424,72"/>
        <polygon points="461,65 472,46 494,46 505,65 494,84 472,84"/>
      </g>
      <polygon points="70,128 124,128 194,184 194,208 120,234 62,242 26,226" fill="url(#gStairs)" opacity="0.85" role="img" aria-label="Staircase illustration with five steps and small icons"/>
      <g>
        <rect x="273" y="112" width="16" height="16" fill="var(--green)"/><polyline points="277,120 281,124 286,116" fill="none" stroke="var(--white)" stroke-width="2"/>
        <rect x="273" y="144" width="16" height="16" fill="var(--blue)"/><polyline points="277,152 281,156 286,148" fill="none" stroke="var(--white)" stroke-width="2"/>
        <rect x="273" y="176" width="16" height="16" fill="var(--green)"/><polyline points="277,184 281,188 286,180" fill="none" stroke="var(--white)" stroke-width="2"/>
        <rect x="273" y="208" width="16" height="16" fill="var(--blue)"/><polyline points="277,216 281,220 286,212" fill="none" stroke="var(--white)" stroke-width="2"/>
        <rect x="273" y="240" width="16" height="16" fill="var(--green)"/><polyline points="277,248 281,252 286,244" fill="none" stroke="var(--white)" stroke-width="2"/>
      </g>
      <g class="kicker">
        <text x="297" y="114">YOUR TITLE HERE</text><text x="297" y="146">YOUR TITLE HERE</text><text x="297" y="178">YOUR TITLE HERE</text><text x="297" y="210">YOUR TITLE HERE</text><text x="297" y="242">YOUR TITLE HERE</text>
      </g>
      <g class="body" style="font-size:4.6px">
        <text x="297" y="122">There are many variations of passages of lorem</text><text x="297" y="128">ipsum available.</text>
        <text x="297" y="154">There are many variations of passages of lorem</text><text x="297" y="160">ipsum available.</text>
        <text x="297" y="186">There are many variations of passages of lorem</text><text x="297" y="192">ipsum available.</text>
        <text x="297" y="218">There are many variations of passages of lorem</text><text x="297" y="224">ipsum available.</text>
        <text x="297" y="250">There are many variations of passages of lorem</text><text x="297" y="256">ipsum available.</text>
      </g>
    </svg>
  </section>

  <!-- Closing -->
  <section class="slide c4 r3">
    <svg viewBox="0 0 530 298">
      <polygon points="258,0 440,0 400,80 300,80" fill="var(--green)"/>
      <polygon points="455,298 530,228 530,298" fill="var(--green)"/>
      <g fill="none" stroke="var(--green)" stroke-width="3">
        <polygon points="414,32 425,13 447,13 458,32 447,51 425,51"/>
        <polygon points="465,12 480,-14 510,-14 525,12 510,38 480,38"/>
        <polygon points="283,275 294.5,255 317.5,255 329,275 317.5,295 294.5,295"/>
        <polygon points="11,55 23,34 47,34 59,55 47,76 23,76"/>
        <polygon points="-26,233 -8,202 28,202 46,233 28,264 -8,264"/>
      </g>
      <polygon points="472,253 481,237 499,237 508,253 499,269 481,269" fill="none" stroke="var(--white)" stroke-width="2.5"/>
      <polygon points="11,151 90,15 247,15 326,151 247,287 90,287" fill="url(#gStone)" role="img" aria-label="Elephant balancing a juggling performer photo"/>
      <text class="display" x="340" y="152" fill="var(--blue)" style="font-size:20px">THANK</text>
      <text class="display" x="340" y="174" fill="var(--blue)" style="font-size:20px">YOU</text>
      <rect x="280" y="186" width="128" height="2" fill="var(--blue)"/>
      <g fill="var(--green)">
        <circle cx="348" cy="232" r="7"/><circle cx="392" cy="232" r="7"/><circle cx="436" cy="232" r="7"/>
      </g>
      <g fill="none" stroke="var(--white)" stroke-width="1.2">
        <path d="M345,229 q0,6 6,6"/>
        <rect x="388" y="229.5" width="8" height="5.5"/><polyline points="388,229.5 392,233 396,229.5"/>
        <circle cx="436" cy="232" r="3.5"/><line x1="432.5" y1="232" x2="439.5" y2="232"/>
      </g>
    </svg>
  </section>

</main>
</body>
</html>
```